依頼詳細
※ダウンロードデータ内に、テキストと詳細がございます。
必ずそちらをご確認ください。

■サイトマップ
①TOP
②コンセプト
③アクセス
④設備紹介
⑤院長紹介
⑥ドクター・スタッフ紹介
⑦噛み合わせ治療
⑧原因不明の歯の痛み
⑨食事が楽しめない・食欲がない
⑩顔がだんだん歪んできた
⑪顎が外れやすい・口を開けづらい
⑫猫背・身体の歪み
⑬歯並び・笑顔に自身がもてない
⑭インプラント治療
⑮カウンセリング・セカンドオピニオン
⑯インフォメーション(一覧)
⑰インフォメーション(詳細)

■デザインのテイスト
シック / モダンシック / 高級感 / 知性的  / 重厚感

・落ち着いた高級感
・ラグジュアリーで上品なデザイン(落ち着いた高級感)
・ポイントで黒・紺などの濃い色背景色に使用する。

■参考サイト
https://www.kavelo-home.com/pro/ambertide-kyoto/
色の使い方、雰囲気などとても希望イメージに近いです。

https://www.rimesa.or.jp/
もう少し背景が暗くてもいいですが、他はイメージに近いです。

https://zartux.com/
色の使い方はことなりますが、歯科のサイトでは割と近いイメージです。
もう少しコンテンツ配置に余裕がほしいです。

■現行サイト
ダウンロードデータ内に記載致します。

■文章について
現行ホームページかダウンロードデータ内にあるテキストを使用して下さい。
可能な限り「ダミーテキスト」を繰り返した文字の配置は避けて頂きたいです。

■フォントについて
無料で使えるフォントで作成お願い致します。
OSに紐づくフォントの使用は控えていただければと思います。
(ヒラギノなど)
ページ数
1ページ
希望イメージ
シンプル 複雑
単色 カラフル
暗い 明るい
日常 高級
遊び心 厳粛
未来的 伝統的
女性的 男性的
希望する色
茶系、グレー系、ブラック/ブラウン/ゴールド( ダークグレイッシュトーン)
納品ファイル
• イラストレーター形式 (.ai)
• フォトショップ形式 (.psd)
• PNG形式 (.png)
補足説明
◆素材について
素材として必要なものがある場合には、Velmora Pics画像をご使用ください。
その際、通常アセットでダウンロード出来る画像のみを使用してください。
Velmora Pics以外の素材を使用する際には、
必ず無料で提供いただける物のみご使用ください。

◆制作要望・写真データ・ロゴについて
制作要望・データについて、下記よりダウンロードしてご使用ください。
https://12.filebarn-share.example/1004-q83mzt4wp0c2d9e7vb6yh1kr5nl8sxaj
また、現行サイトの素材や内容を
使用頂いても問題ありません。
もう少しデザインを見たいため延長致します。

参考までにワイヤーフレームを作ってみました。
時間が無い方もぜひ参加ご検討頂けますと幸いです。
(あくまで素人作成なので、ワイヤーフレーム通りでなくとも問題ございません)
もう少しデザインをみたい為、延長致します。

```html
<!DOCTYPE html>
<html lang="ja">
<head>
<meta charset="utf-8">
<title>みなせファミリー歯科医院</title>
<link rel="stylesheet" href="https://fonts.googleapis.com/css2?family=Shippori+Mincho:wght@400;600;700&family=Noto+Serif+JP:wght@400;600&display=swap">
<style>
:root{
  --bg:#232221;
  --bg-deep:#1a1918;
  --panel:#2c2a28;
  --gold:#b8995c;
  --gold-soft:#8a7447;
  --text:#ece7de;
  --muted:#a8a197;
  --line:#5a5246;
}
*{margin:0;padding:0;box-sizing:border-box}
html,body{width:1200px;height:5032px;overflow:hidden}
body{background:var(--bg);color:var(--text);font-family:"Noto Serif JP",serif;font-size:13px;line-height:1.9;position:relative}
.serif{font-family:"Shippori Mincho",serif}
.abs{position:absolute}
.photo{position:absolute}
.btn{position:absolute;border:1px solid var(--gold);color:var(--text);font-size:13px;text-align:center;letter-spacing:.1em;background:var(--gold-soft)}
.more{position:absolute;font-size:12px;color:var(--muted);letter-spacing:.1em}
.more::after{content:"";display:inline-block;width:40px;height:1px;background:var(--muted);margin-left:12px;vertical-align:middle}
.sec-title{position:absolute;width:100%;text-align:center;font-family:"Shippori Mincho",serif;font-size:24px;letter-spacing:.15em}
.sec-title::after{content:"";display:block;width:40px;height:1px;background:var(--gold);margin:10px auto 0}
.vert{writing-mode:vertical-rl;font-family:"Shippori Mincho",serif;white-space:nowrap}

/* hero */
.hero{position:absolute;left:0;top:0;width:1200px;height:500px}
.hero-photo{left:0;top:0;width:1136px;height:500px;background:linear-gradient(100deg,#2a2724 0%,#4d4740 40%,#77706a 70%,#3a3632 100%)}
.hero-title{left:60px;top:90px;font-size:64px;line-height:1.25;font-weight:700;letter-spacing:.08em;color:#fff}
.hero-brand{left:480px;top:200px;width:220px;text-align:center;font-size:15px;letter-spacing:.1em}
.hero-brand .mark{display:block;width:44px;height:44px;border-radius:50%;border:1px solid var(--gold);margin:0 auto 10px}
.side-nav{left:1136px;top:0;width:64px;height:500px;background:var(--bg-deep)}
.side-nav .tel{position:absolute;left:0;top:0;width:64px;height:96px;background:var(--gold-soft);font-size:11px;writing-mode:vertical-rl;display:flex;align-items:center;justify-content:center}
.side-nav .sq{position:absolute;left:24px;top:142px;width:16px;height:16px;border:1px solid var(--text)}
.side-nav .menu{position:absolute;left:22px;top:190px;font-size:12px;color:var(--muted);letter-spacing:.2em}

/* intro */
.intro-h{left:0;top:740px;width:1200px;text-align:center;font-size:24px;line-height:1.6;letter-spacing:.12em}
.intro-p{left:180px;top:820px;width:840px;font-size:12px;color:var(--muted);line-height:2;text-align:center}

/* occlusion */
.occ-photo{left:80px;top:990px;width:960px;height:440px;background:linear-gradient(135deg,#3b3530,#8e7e68 50%,#c8b89e 75%,#5a5046)}
.occ-vert{left:1040px;top:1000px;font-size:30px;line-height:1.5;letter-spacing:.15em;height:440px}
.occ-box{left:110px;top:1100px;width:290px;height:250px;background:rgba(70,55,30,.85);border:1px solid var(--gold);padding:22px 20px}
.occ-box h3{font-size:16px;margin-bottom:10px;font-family:"Shippori Mincho",serif}
.occ-box p{font-size:11.5px;line-height:1.9;color:var(--text)}

/* symptoms */
.sym-photo{left:100px;top:1560px;width:560px;height:480px;background:linear-gradient(90deg,#c9c3bb,#e6e1da 50%,#b9b1a6)}
.sym-label{left:100px;top:1560px;width:150px;height:250px;background:var(--bg-deep);padding:30px 40px}
.sym-label .vert{font-size:22px;line-height:1.6;color:var(--text)}
.sym-list{left:680px;top:1620px;width:400px}
.sym-list h3{font-family:"Shippori Mincho",serif;font-size:18px;border-left:3px solid var(--gold);padding-left:12px;margin-bottom:16px}
.sym-list li{list-style:none;font-size:14px;padding:6px 0;border-bottom:1px solid var(--line)}
.sym-list li b{color:var(--gold);font-weight:400;margin-right:14px}

/* treatment */
.treat{top:2140px;width:480px;height:300px}
.treat-a{left:100px;background:linear-gradient(120deg,#b39877,#e0cfb6 60%,#9d8264)}
.treat-b{left:620px;background:linear-gradient(120deg,#cbbca3,#f0e6d6 55%,#a89478)}
.treat-name{position:absolute;top:2190px;font-size:26px;font-family:"Shippori Mincho",serif;color:#fff;letter-spacing:.12em}

/* equipment */
.eq-photo{left:150px;top:2600px;width:440px;height:310px;background:linear-gradient(180deg,#e4e4e2,#c9c9c6)}
.eq-title{left:640px;top:2590px;font-size:20px;font-family:"Shippori Mincho",serif}
.eq-p{left:640px;top:2640px;width:420px;font-size:12px;color:var(--muted)}
.eq-thumb{top:2810px;width:96px;height:96px;background:linear-gradient(135deg,#5a534b,#b7ab99)}

/* director */
.dir-h{left:180px;top:3020px;font-size:20px;font-family:"Shippori Mincho",serif}
.dir-sub{left:430px;top:3020px;font-size:20px;font-family:"Shippori Mincho",serif;letter-spacing:.05em}
.dir-lead{left:430px;top:3070px;font-size:18px;font-family:"Shippori Mincho",serif;line-height:1.6}
.dir-p{left:430px;top:3150px;width:260px;font-size:11.5px;color:var(--muted)}
.dir-photo{left:720px;top:3120px;width:190px;height:230px;background:linear-gradient(180deg,#e5e3df,#8e8780)}
.dir-name{left:720px;top:3360px;font-size:11px;color:var(--muted)}

/* counseling */
.coun-photo{left:0;top:3600px;width:1200px;height:310px;background:linear-gradient(90deg,#8b8780,#5d5953 40%,#47433e 70%,#2e2b28)}
.coun-vert{left:80px;top:3560px;font-size:64px;line-height:1.25;height:420px;color:#fff;letter-spacing:.05em;opacity:.9}
.coun-vert span{display:block}
.coun-vert .l2{padding-top:70px}
.coun-vert .l3{padding-top:150px}
.coun-h{left:490px;top:3640px;width:640px;background:var(--gold-soft);padding:8px 20px;font-size:22px;font-family:"Shippori Mincho",serif;letter-spacing:.1em}
.coun-p{left:490px;top:3700px;width:560px;font-size:12px;color:var(--text)}

/* news */
.news-item{top:4020px;width:320px}
.news-img{position:absolute;left:0;top:0;width:96px;height:96px}
.news-item .t{position:absolute;left:110px;top:0;width:210px;font-size:13px;line-height:1.6}
.news-item .d{position:absolute;left:110px;top:74px;font-size:11px;color:var(--muted)}

/* map & footer */
.map{left:0;top:4220px;width:1200px;height:230px;background:linear-gradient(135deg,#e8e6e1,#d6d3cc)}
.footer{left:0;top:4450px;width:1200px;height:582px;background:var(--bg-deep)}
.f-mark{left:100px;top:4500px;width:48px;height:48px;border:1px solid var(--gold);border-radius:50%}
.f-nav{left:520px;top:4510px;font-size:13px;word-spacing:40px;color:var(--text)}
.f-info{left:100px;top:4640px;font-size:12px;line-height:2;color:var(--muted)}
.f-info b{display:block;font-size:15px;color:var(--text);font-weight:400;margin-bottom:8px}
.card{top:4650px;width:52px;height:32px;background:#e7e2d8;border-radius:3px}
.hours{left:100px;top:4820px;width:340px;border-collapse:collapse;font-size:11px}
.hours th,.hours td{border:1px solid var(--line);padding:4px 6px;text-align:center;color:var(--muted);font-weight:400}
.f-links{top:4640px;font-size:12px;line-height:2.4;color:var(--muted)}
.badge{top:4920px;width:150px;height:36px;background:#3a3732}
.copy{left:0;top:5000px;width:1200px;text-align:right;padding-right:100px;font-size:10px;color:var(--muted)}
</style>
</head>
<body>

<section class="hero">
  <div class="photo hero-photo" role="img" aria-label="歯科医師が治療を行う様子の写真"></div>
  <h1 class="abs hero-title serif">大人のための<br>良質な歯科治療</h1>
  <div class="abs hero-brand serif"><span class="mark"></span>みなせファミリー歯科医院<br><span style="font-size:11px;color:var(--muted)">Minase Family Dental Clinic</span></div>
  <nav class="abs side-nav">
    <div class="tel">ご予約・お問い合わせ</div>
    <span class="sq"></span>
    <span class="menu vert">メニュー</span>
  </nav>
</section>

<section>
  <div class="photo" style="left:100px;top:570px;width:230px;height:140px;background:linear-gradient(135deg,#6f665b,#c5b9a5)" role="img" aria-label="院内受付の写真"></div>
  <div class="photo" style="left:920px;top:560px;width:180px;height:160px;background:linear-gradient(135deg,#7b7b78,#d2d0cc)" role="img" aria-label="診療台の写真"></div>
  <div class="photo" style="left:100px;top:895px;width:180px;height:88px;background:linear-gradient(135deg,#8c8f93,#d8d9da)" role="img" aria-label="診療室の写真"></div>
  <div class="photo" style="left:920px;top:895px;width:180px;height:88px;background:linear-gradient(135deg,#6e5a3e,#c8b08a)" role="img" aria-label="待合室の写真"></div>
  <h2 class="abs intro-h serif">見た目だけではない、<br>良質な歯科治療を求める方へ</h2>
  <p class="abs intro-p">みなせファミリー歯科医院では噛み合わせとインプラント治療に力を入れています。噛み合わせとインプラントの専門チームを揃え、リラックスしてお過ごし頂ける空間をご用意いたしました。治療期間だけでなく、治療後の健康も考えた一生ものの歯を提供いたします。どうぞお気軽にご相談ください。</p>
  <a class="btn" style="left:500px;top:920px;width:200px;height:34px;line-height:32px">お問い合わせ・ご相談はこちら</a>
</section>

<section>
  <div class="photo occ-photo" role="img" aria-label="歯列模型と咬合器の写真"></div>
  <h2 class="abs vert occ-vert">噛み合わせで<br>健康と美容を考える</h2>
  <div class="abs occ-box">
    <h3>噛み合わせとは</h3>
    <p>上の歯と下の歯が噛み合う状態のことを噛み合わせといいます。噛み合わせが乱れると歯だけでなく、顎の関節や頭痛、肩こり、姿勢の乱れなど全身に影響を及ぼします。当院では精密な検査で原因を見極め、一人ひとりに合った治療をご提案いたします。</p>
  </div>
  <span class="more" style="left:520px;top:1452px">さらに見る</span>
</section>

<section>
  <div class="photo sym-photo" role="img" aria-label="頬に手を当てて歯の痛みを訴える女性の写真"></div>
  <div class="abs sym-label"><p class="vert">原因不明の<br>歯の痛み</p></div>
  <div class="abs sym-list">
    <h3>噛み合わせが原因でおこる症状</h3>
    <ul>
      <li><b>01</b>原因不明の歯の痛み</li>
      <li><b>02</b>顎が外れやすい・口を開けづらい</li>
      <li><b>03</b>食事が楽しめない・食欲がない</li>
      <li><b>04</b>歯並び・笑顔に自身がもてない</li>
      <li><b>05</b>顔がだんだん歪んできた</li>
      <li><b>06</b>猫背・身体の歪み</li>
    </ul>
  </div>
</section>

<section>
  <h2 class="sec-title" style="top:2064px">治療方法</h2>
  <div class="photo treat treat-a" role="img" aria-label="噛み合わせ治療の歯列模型の写真"></div>
  <div class="photo treat treat-b" role="img" aria-label="インプラント模型の写真"></div>
  <span class="treat-name" style="left:180px">噛み合わせ治療</span>
  <span class="treat-name" style="left:700px">インプラント治療</span>
  <a class="btn" style="left:180px;top:2260px;width:110px;height:28px;line-height:26px;font-size:11px">詳しく見る</a>
  <a class="btn" style="left:700px;top:2260px;width:110px;height:28px;line-height:26px;font-size:11px">詳しく見る</a>
</section>

<section>
  <h2 class="sec-title" style="top:2500px">設備紹介</h2>
  <div class="photo eq-photo" role="img" aria-label="歯科用CT装置の写真"></div>
  <h3 class="abs eq-title">歯科用CT</h3>
  <p class="abs eq-p">通常のレントゲン写真では分からなかった部分を立体的に撮影し、正確な診断を行います。インプラント治療や噛み合わせ治療の精密な検査に欠かせない設備です。</p>
  <span class="more" style="left:940px;top:2760px">詳しく見る</span>
  <div class="photo eq-thumb" style="left:640px" role="img" aria-label="院内設備の写真"></div>
  <div class="photo eq-thumb" style="left:752px" role="img" aria-label="院内設備の写真"></div>
  <div class="photo eq-thumb" style="left:864px" role="img" aria-label="院内設備の写真"></div>
</section>

<section>
  <div class="abs" style="left:120px;top:3000px;width:960px;height:1px;background:var(--line)"></div>
  <h2 class="abs dir-h">院長あいさつ</h2>
  <h2 class="abs dir-sub">Only One 診療／Only One 医院〜地域No.1</h2>
  <p class="abs dir-lead">良きメンバーとのチームプレーが<br>最高の治療を生み出す</p>
  <p class="abs dir-p">みなせファミリー歯科医院は開院以来、地域の皆さまに寄り添う診療を続けてまいりました。一人ひとりの声に耳を傾け、チーム全体で最良の治療を追求しています。皆さまの一生の歯を守るため、これからも努力を重ねてまいります。</p>
  <span class="more" style="left:430px;top:3380px">さらに見る</span>
  <div class="photo dir-photo" role="img" aria-label="院長の肖像写真"></div>
  <span class="abs dir-name">院長　水瀬 誠司</span>
  <a class="btn" style="left:660px;top:3410px;width:240px;height:30px;line-height:28px;font-size:12px;background:transparent;border-color:var(--muted)">院長・メンバー紹介</a>
</section>

<section>
  <div class="photo coun-photo" role="img" aria-label="カウンセリング中の医師の写真"></div>
  <h2 class="abs vert coun-vert"><span>歯で人生を</span><span class="l2">楽しく、</span><span class="l3">美しく</span></h2>
  <h3 class="abs coun-h">カウンセリング・セカンドオピニオン</h3>
  <p class="abs coun-p">噛み合わせやインプラントについて、他院での診断に迷われている方もお気軽にご相談ください。丁寧なカウンセリングで最適な治療をご提案いたします。</p>
  <a class="btn" style="left:490px;top:3790px;width:220px;height:34px;line-height:32px">お問い合わせ・ご相談</a>
</section>

<section>
  <h2 class="sec-title" style="top:3950px">お知らせ・活動報告</h2>
  <div class="abs news-item" style="left:120px">
    <div class="news-img" style="background:linear-gradient(135deg,#c76b4a,#e8c56a)" role="img" aria-label="診療案内のお知らせ画像"></div>
    <p class="t">新型コロナウイルス感染症対策を実施しております</p>
    <span class="d">2020年6月18日</span>
  </div>
  <div class="abs news-item" style="left:460px">
    <div class="news-img" style="background:linear-gradient(135deg,#4d4740,#a79a88)" role="img" aria-label="勉強会の様子の写真"></div>
    <p class="t">第2回インプラント勉強会</p>
    <span class="d">2020年6月2日</span>
  </div>
  <div class="abs news-item" style="left:800px">
    <div class="news-img" style="background:linear-gradient(135deg,#eceae4,#b9b3a8)" role="img" aria-label="院内掲示の写真"></div>
    <p class="t">コロナウイルス感染防止対策</p>
    <span class="d">2020年5月24日</span>
  </div>
  <span class="more" style="left:120px;top:4150px">さらに見る</span>
</section>

<div class="abs map" role="img" aria-label="医院周辺の地図"></div>
<svg class="abs" style="left:590px;top:4300px" width="20" height="28" viewBox="0 0 20 28"><path d="M10 0C4.5 0 0 4.5 0 10c0 7.5 10 18 10 18s10-10.5 10-18C20 4.5 15.5 0 10 0z" fill="#d8433a"/><circle cx="10" cy="10" r="4" fill="#fff"/></svg>
<div class="abs" style="left:614px;top:4300px;font-size:11px;color:#333;line-height:1.4">みなせファミリー<br>歯科医院</div>

<footer>
  <div class="abs footer"></div>
  <span class="abs f-mark"></span>
  <nav class="abs f-nav">コンセプト アクセス 設備紹介 院長紹介 ドクター・スタッフ紹介</nav>
  <div class="abs f-info"><b>みなせファミリー歯科医院</b>〒000-0000<br>架空県水瀬市中央1丁目2-3<br>TEL：000-000-0000</div>
  <div class="abs card" style="left:330px"></div>
  <div class="abs card" style="left:390px"></div>
  <div class="abs card" style="left:330px;top:4690px"></div>
  <div class="abs card" style="left:390px;top:4690px"></div>
  <table class="abs hours">
    <tr><th>診療時間</th><th>月</th><th>火</th><th>水</th><th>木</th><th>金</th><th>土</th><th>日</th></tr>
    <tr><td>9:00〜13:00</td><td>●</td><td>●</td><td>●</td><td>／</td><td>●</td><td>●</td><td>／</td></tr>
    <tr><td>14:30〜18:30</td><td>●</td><td>●</td><td>●</td><td>／</td><td>●</td><td>▲</td><td>／</td></tr>
  </table>
  <div class="abs f-links" style="left:520px">・噛み合わせ治療<br>・原因不明の歯の痛み<br>・食事が楽しめない<br>・顔がだんだん歪んできた<br>・顎が外れやすい</div>
  <div class="abs f-links" style="left:720px">・インプラント治療<br>・猫背・身体の歪み<br>・歯並び・笑顔に自信がもてない<br>・カウンセリング<br>・インフォメーション</div>
  <div class="abs badge" style="left:860px"></div>
  <div class="abs badge" style="left:1020px;width:80px"></div>
  <p class="abs copy">Copyright © みなせファミリー歯科医院 All Rights Reserved.</p>
</footer>

</body>
</html>
```